Webdesign für Selbsthilfegruppe für Gehörlose
Zielgruppe
(Un)gesehene Schwestern Chemnitz und Umgebung ist eine Selbsthilfegruppe
Wir sind eine Gruppe von Frauen mit und ohne Hörschädigungen sowie Traumaerfahrungen.
Die SHG berät allen Arten der Hörschädigung und Traumafolgen von betroffene Frauen.
Schwerpunkte der Arbeit:
Zurück in das ICH finden mit Unterstützung, Aufklärung, Erkennen, Benennen, Handlen und Vermittlung von Behandlungen sowie Rehabilitation und Rückfallprävention
Weiteres entnehmen Sie bitte aus dem Flyer
Aufgabenstellung
Barrierefreiheit der Website für Menschen mit Hörbehinderung

```html
<!DOCTYPE html>
<html lang="de">
<head>
<meta charset="utf-8">
<title>(Un)gesehene Schwestern – Selbsthilfegruppe Chemnitz</title>
<link href="https://fonts.googleapis.com/css2?family=Open+Sans:wght@300;400;600;700&display=swap" rel="stylesheet">
<style>
:root{
  --cream:#fcf5ef;
  --mint:#cfe0d4;
  --sage:#7bb79b;
  --sage-dark:#4f8f72;
  --leaf:#2d7d2f;
  --ink:#333333;
  --text:#555555;
  --white:#ffffff;
}
*{box-sizing:border-box;margin:0;padding:0}
html,body{width:1200px;height:2421px;overflow:hidden}
body{font-family:"Open Sans",Arial,sans-serif;color:var(--ink);background:var(--white);position:relative}
.abs{position:absolute}

/* header */
.site-header{left:0;top:0;width:1200px;height:122px;background:var(--white)}
.brand{left:160px;top:16px;width:120px;height:92px;display:flex;flex-direction:column;align-items:center;gap:6px}
.brand-dot{width:48px;height:48px;border-radius:50%;border:2px solid var(--ink)}
.brand-name{font-size:10px;font-weight:600;color:var(--ink);text-align:center;line-height:1.2}
.contact-tab{left:552px;top:0;width:95px;height:28px;background:var(--sage);border-radius:0 0 10px 10px;display:flex;justify-content:center;align-items:center;gap:18px}
.main-nav{left:0;top:98px;width:1200px;text-align:center;font-size:9px;color:var(--ink);letter-spacing:.2px}
.main-nav span{padding:0 1px}
.main-nav .active{border-bottom:2px solid var(--sage);padding-bottom:3px}

/* hero */
.hero{left:0;top:122px;width:1200px;height:456px;background:var(--cream)}
.branch-art{left:0;top:122px;width:375px;height:275px;background:radial-gradient(ellipse at 20% 45%,#3f8a3a 0%,#6fae5a 40%,rgba(252,245,239,0) 72%)}
.hero-box{left:264px;top:241px;width:673px;height:223px;border:1px solid #555;text-align:center;padding-top:12px}
.hero-box h1{font-size:23px;font-weight:600;letter-spacing:1px;line-height:27px;color:var(--ink);margin-top:6px}
.hero-box .lead{font-size:9px;line-height:15px;margin-top:16px;color:var(--ink)}
.hero-box .addr{font-size:10.5px;line-height:15px;margin-top:14px;color:var(--ink)}

/* icon band */
.topic-band{left:0;top:578px;width:1200px;height:331px;background:var(--mint)}
.topic{width:141px;height:141px;border-radius:50%;background:var(--sage);display:flex;flex-direction:column;align-items:center;justify-content:center;color:var(--white);font-size:10px;font-weight:700;letter-spacing:.3px}
.topic svg{margin-bottom:8px}

/* photo slider */
.slider{left:0;top:909px;width:1200px;height:406px;background:linear-gradient(180deg,#e9cfc0 0%,#b9c9c2 35%,#5e8f8c 65%,#3f6f70 100%)}
.slogan{left:0;top:1160px;width:1200px;text-align:center;color:var(--white);font-size:30px;font-weight:700;line-height:38px;letter-spacing:.5px;text-shadow:0 2px 6px rgba(0,0,0,.35)}

/* focus section */
.focus{left:0;top:1315px;width:1200px;height:736px;background:var(--sage)}
.foliage-art{left:836px;top:1654px;width:364px;height:397px;background:radial-gradient(ellipse at 75% 60%,#2e7a36 0%,#5f9d45 40%,rgba(123,183,155,0) 72%)}
.card{width:402px;height:397px;background:var(--cream);box-shadow:5px 5px 0 var(--sage-dark);padding:12px 24px}
.card-head{text-align:center;border-bottom:1px solid #777;padding-bottom:8px}
.card-head h2{font-size:18px;font-weight:600;letter-spacing:.4px;margin-top:4px;color:var(--ink)}
.card ul{list-style:none;margin-top:24px}
.card li{font-size:10px;line-height:22.5px;color:var(--text);display:flex;align-items:center;gap:6px}
.btn{left:472px;top:1912px;width:252px;height:72px;border-radius:36px;background:var(--cream);color:var(--sage);font-size:15px;font-weight:600;display:flex;align-items:center;justify-content:center;letter-spacing:.5px}

/* more */
.more{left:0;top:2051px;width:1200px;height:318px;background:var(--cream)}
.site-footer{left:0;top:2369px;width:1200px;height:52px;background:var(--white);text-align:center;font-size:8.5px;padding-top:18px;color:var(--ink)}
</style>
</head>
<body>

<header class="abs site-header">
  <div class="abs brand"><div class="brand-dot"></div><div class="brand-name">(Un)gesehene Schwestern</div></div>
  <div class="abs contact-tab">
    <svg width="16" height="11" viewBox="0 0 16 11"><path d="M1 4 Q8 -1 15 4 L13 6 L11 4 L5 4 L3 6 Z M4 6 H12 V10 H4 Z" fill="#fff"/></svg>
    <svg width="16" height="11" viewBox="0 0 16 11" fill="none" stroke="#fff"><rect x="1" y="1" width="14" height="9"/><path d="M1 1 L8 6 L15 1"/></svg>
  </div>
  <nav class="abs main-nav"><span>HOME</span>|<span>ÜBER UNS</span>|<span class="active">DAS TEAM</span>|<span>DAS TRAUMA</span>|<span>HÖRSCHÄDIGUNG</span>|<span>NETZWERK</span>|<span>PARTNER</span>|<span>AKTUELLES</span>|<span>FÖRDERER</span></nav>
</header>

<section class="abs hero"></section>
<div class="abs branch-art" role="img" aria-label="Illustration eines grünen Astes mit Blättern"></div>
<div class="abs hero-box">
  <svg width="26" height="26" viewBox="0 0 26 26"><path d="M6 22 Q4 10 18 4 Q20 16 6 22Z" fill="var(--leaf)"/><path d="M4 24 Q12 18 22 20" stroke="var(--leaf)" stroke-width="2" fill="none"/></svg>
  <h1>(UN)GESEHENE SCHWESTERN<br>DIE SELBSTHILFEGRUPPE IN CHEMNITZ UND UMLAND</h1>
  <p class="lead">Anlaufstelle für Frauen, die von allen Arten der Hörschädigung und Traumafolgestörungen betroffene sind,<br>und Frauen ohne diese Beiträchtigungen.</p>
  <p class="addr">Lindenhofweg 14 | 09113 Chemnitz<br>☎ +49 151 20573418 oder +49 1746208315<br>✉ ungeseheneschwestern@post-mail.de</p>
</div>

<section class="abs topic-band"></section>
<div class="abs topic" style="left:246px;top:687px">
  <svg width="80" height="66" viewBox="0 0 80 66" fill="none" stroke="#fff" stroke-width="4" stroke-linecap="round"><path d="M2 38 H14 L20 26 L26 48 L31 36 H40"/><path d="M44 50 Q52 66 62 56 Q66 50 70 42 Q78 24 66 10 Q52 0 42 14 Q38 22 44 28 Q50 32 46 40"/></svg>
  HÖRSCHÄDIGUNG
</div>
<div class="abs topic" style="left:435px;top:687px">
  <svg width="66" height="66" viewBox="0 0 66 66" fill="none" stroke="#fff" stroke-width="3.5" stroke-linecap="round"><circle cx="40" cy="12" r="8"/><path d="M26 30 Q30 22 40 26 Q46 36 42 48 L34 62 M26 30 L16 44 L30 54 L22 62 M44 34 L56 40"/><path d="M8 20 q3 4 0 8 q-3 4 0 8 M58 10 q3 4 0 8 q-3 4 0 8"/></svg>
  TRAUMA
</div>
<div class="abs topic" style="left:619px;top:687px">
  <svg width="66" height="66" viewBox="0 0 66 66" fill="none" stroke="#fff" stroke-width="3"><circle cx="33" cy="8" r="5"/><path d="M24 24 Q33 12 42 24Z"/><circle cx="22" cy="30" r="5"/><circle cx="44" cy="30" r="5"/><path d="M12 44 Q22 34 32 44Z M34 44 Q44 34 54 44Z"/><circle cx="12" cy="50" r="4.5"/><circle cx="33" cy="50" r="4.5"/><circle cx="54" cy="50" r="4.5"/><path d="M3 63 Q12 54 21 63 M24 63 Q33 54 42 63 M45 63 Q54 54 63 63"/></svg>
  TEAM
</div>
<div class="abs topic" style="left:813px;top:687px">
  <svg width="66" height="66" viewBox="0 0 66 66" fill="none" stroke="#fff" stroke-width="3.5"><circle cx="12" cy="10" r="6"/><path d="M2 24 Q12 14 22 24Z"/><circle cx="54" cy="10" r="6"/><path d="M44 24 Q54 14 64 24Z"/><circle cx="33" cy="36" r="8"/><path d="M17 62 Q33 42 49 62Z"/><path d="M22 12 Q33 4 44 12 M6 30 Q8 48 18 54 M60 30 Q58 48 48 54"/></svg>
  NETZWERK
</div>

<section class="abs slider" role="img" aria-label="Foto: Frau mit ausgebreiteten Armen vor einem Bergpanorama"></section>
<svg class="abs" style="left:45px;top:1095px" width="58" height="63" viewBox="0 0 58 63"><path d="M58 0 L0 31.5 L58 63 L30 31.5Z" fill="var(--sage)"/></svg>
<svg class="abs" style="left:1097px;top:1095px" width="58" height="63" viewBox="0 0 58 63"><path d="M0 0 L58 31.5 L0 63 L28 31.5Z" fill="var(--sage)"/></svg>
<div class="abs slogan">FINDE ZURÜCK ZU DIR UND<br>ERFAHRE LEBENSFREUDE UND LEICHTIGKEIT</div>

<section class="abs focus"></section>
<div class="abs foliage-art" role="img" aria-label="Illustration eines belaubten Zweiges"></div>

<article class="abs card" style="left:176px;top:1452px">
  <div class="card-head">
    <svg width="30" height="22" viewBox="0 0 30 22" fill="none" stroke="#555" stroke-width="1.5"><path d="M2 12 Q15 0 28 12 Q15 24 2 12Z"/><circle cx="15" cy="12" r="4"/><path d="M15 1 V4 M6 3 L8 6 M24 3 L22 6"/></svg>
    <h2>UNSERE SCHWERPUNKTE</h2>
  </div>
  <ul>
    <li><svg width="10" height="9"><path d="M1 4 L4 8 L9 1" stroke="var(--leaf)" stroke-width="2.5" fill="none"/></svg>Aufklären</li>
    <li><svg width="10" height="9"><path d="M1 4 L4 8 L9 1" stroke="var(--leaf)" stroke-width="2.5" fill="none"/></svg>Benennen</li>
    <li><svg width="10" height="9"><path d="M1 4 L4 8 L9 1" stroke="var(--leaf)" stroke-width="2.5" fill="none"/></svg>Erkennen</li>
    <li><svg width="10" height="9"><path d="M1 4 L4 8 L9 1" stroke="var(--leaf)" stroke-width="2.5" fill="none"/></svg>Handlen /Vermittlung von Behandlung</li>
    <li><svg width="10" height="9"><path d="M1 4 L4 8 L9 1" stroke="var(--leaf)" stroke-width="2.5" fill="none"/></svg>Vermittlung von Rehabilitation</li>
    <li><svg width="10" height="9"><path d="M1 4 L4 8 L9 1" stroke="var(--leaf)" stroke-width="2.5" fill="none"/></svg>Rückfallprävention</li>
  </ul>
</article>

<article class="abs card" style="left:622px;top:1452px">
  <div class="card-head">
    <svg width="30" height="26" viewBox="0 0 30 26" fill="none" stroke="#555" stroke-width="1.5"><circle cx="13" cy="14" r="10"/><circle cx="13" cy="14" r="6"/><circle cx="13" cy="14" r="2"/><path d="M13 14 L27 2 M23 2 H27 V6"/></svg>
    <h2>UNSERE ZIELE</h2>
  </div>
  <ul>
    <li><svg width="10" height="9"><path d="M1 4 L4 8 L9 1" stroke="var(--leaf)" stroke-width="2.5" fill="none"/></svg>Förderung gesunder Beziehung über Respekt und Achtsamkeit</li>
    <li><svg width="10" height="9"><path d="M1 4 L4 8 L9 1" stroke="var(--leaf)" stroke-width="2.5" fill="none"/></svg>Strategien der geWaltfreien&nbsp; Kommunikation erlernen und anwerden</li>
    <li><svg width="10" height="9"><path d="M1 4 L4 8 L9 1" stroke="var(--leaf)" stroke-width="2.5" fill="none"/></svg>Förderung gesunder Beziehung über Respekt und Achtsamkeit</li>
    <li><svg width="10" height="9"><path d="M1 4 L4 8 L9 1" stroke="var(--leaf)" stroke-width="2.5" fill="none"/></svg>Unterschiede tolerieren lernen</li>
    <li><svg width="10" height="9"><path d="M1 4 L4 8 L9 1" stroke="var(--leaf)" stroke-width="2.5" fill="none"/></svg>Förderung der individuellen Entwicklung</li>
    <li><svg width="10" height="9"><path d="M1 4 L4 8 L9 1" stroke="var(--leaf)" stroke-width="2.5" fill="none"/></svg>Auseinandersetzung mit eigenen Schattenseiten</li>
    <li><svg width="10" height="9"><path d="M1 4 L4 8 L9 1" stroke="var(--leaf)" stroke-width="2.5" fill="none"/></svg>Förderung von Verantwortungsbewusstsein</li>
    <li><svg width="10" height="9"><path d="M1 4 L4 8 L9 1" stroke="var(--leaf)" stroke-width="2.5" fill="none"/></svg>Akzeptanz der Realität und Öffnung für Lösungswege</li>
    <li><svg width="10" height="9"><path d="M1 4 L4 8 L9 1" stroke="var(--leaf)" stroke-width="2.5" fill="none"/></svg>Lebensfreude und Leichtigkeit</li>
    <li><svg width="10" height="9"><path d="M1 4 L4 8 L9 1" stroke="var(--leaf)" stroke-width="2.5" fill="none"/></svg>Gemeinschaft</li>
    <li><svg width="10" height="9"><path d="M1 4 L4 8 L9 1" stroke="var(--leaf)" stroke-width="2.5" fill="none"/></svg>Geben und Nehmen</li>
    <li><svg width="10" height="9"><path d="M1 4 L4 8 L9 1" stroke="var(--leaf)" stroke-width="2.5" fill="none"/></svg>Aufbau und Erhaltung von Selbstwert, Selbstsicherheit u. a. m.</li>
  </ul>
</article>

<div class="abs btn">KONTAKT AUFNEHMEN</div>

<section class="abs more"></section>
<div class="abs topic" style="left:347px;top:2151px">
  <svg width="66" height="66" viewBox="0 0 66 66" fill="none" stroke="#fff" stroke-width="3.5" stroke-linecap="round"><rect x="6" y="8" width="40" height="52" rx="3"/><rect x="18" y="3" width="16" height="9" rx="2"/><path d="M13 24 L16 27 L21 21 M26 24 H38 M13 38 L16 41 L21 35 M26 38 H34"/><circle cx="50" cy="50" r="11" fill="var(--sage)"/><path d="M50 44 V50 H55"/></svg>
  AKTUELLES
</div>
<div class="abs topic" style="left:531px;top:2151px">
  <svg width="70" height="66" viewBox="0 0 70 66" fill="none" stroke="#fff" stroke-width="3.5" stroke-linecap="round"><circle cx="20" cy="12" r="7"/><circle cx="50" cy="12" r="7"/><path d="M8 60 V28 Q8 22 14 22 H26 Q32 22 32 28 V44 M20 60 V40 M38 44 V28 Q38 22 44 22 H56 Q62 22 62 28 V60 M50 60 V40 M32 36 H38"/><path d="M35 2 V6 M28 4 L30 7 M42 4 L40 7"/></svg>
  PARTNER
</div>
<div class="abs topic" style="left:725px;top:2151px">
  <svg width="70" height="60" viewBox="0 0 70 60" fill="none" stroke="#fff" stroke-width="3.5" stroke-linecap="round" stroke-linejoin="round"><path d="M2 12 H16 L30 8 L46 14 H68 M2 34 H10 L30 52 Q34 56 38 52 L56 34 H68 M30 20 L40 28 Q44 30 46 26 L38 16 M20 36 L28 44 M26 30 L36 40 M34 26 L44 36"/></svg>
  FÖRDERER
</div>

<footer class="abs site-footer">KONTAKT | IMPRESSUM | DATENSCHUTZ</footer>

</body>
</html>
```